Premium Juice and Wine Bottle Label

We require a premium label design for a Burgundy style wine bottle - the design should reflect pure and organic theme, with a reference to New Zealand blueberries. The winning design will look high-end, simple but sophisticated. Our logo is attached, refer :

https://www.orvalecellars.co.nz and https://www.pirovane.co.nz/wines/details/coming-soon-showcase/2018

for inspiration.

Target Market(s)

High-end retail grocery stores, wine shops, bars.

Requirements
Must have
• Label should leave enough space for barcode and nutrients/ingredients etc. Reference to New Zealand, natural-beverage, be very high-end in design. Refer links in project description for inspiration. Refer to attached logo, which must be used - feel free to change colour in order to obtain the best high-class design.
Nice to have
• N/A.
Should not have
• Cartoons or pictures of berries.

```html
<!DOCTYPE html>
<html lang="en">
<head>
<meta charset="utf-8">
<title>Kowhai Lane — Wine Labels</title>
<link rel="stylesheet" href="https://fonts.googleapis.com/css2?family=EB+Garamond:ital,wght@0,500;1,400;1,500&family=Nunito+Sans:wght@400;700&display=swap">
<style>
  :root {
    --backdrop: #e2e3e2;
    --label-cream: #f1ebd8;
    --label-edge: #e6dcc0;
    --gold: #cfa95e;
    --gold-light: #e2c68a;
    --gold-text: #d9bd80;
    --plum: #5a1a3a;
    --ink: #4a3038;
    --ink-soft: #5c4a4f;
  }
  * { box-sizing: border-box; margin: 0; padding: 0; }
  html, body {
    width: 1200px;
    height: 921px;
    overflow: hidden;
    background: var(--backdrop);
  }
  .canvas {
    position: relative;
    width: 1200px;
    height: 921px;
    display: flex;
    justify-content: center;
    align-items: center;
    gap: 60px;
  }
  .label {
    position: relative;
    width: 320px;
    height: 500px;
    background: linear-gradient(90deg, var(--label-edge) 0%, var(--label-cream) 12%, var(--label-cream) 88%, var(--label-edge) 100%);
    border: 5px solid var(--gold);
    box-shadow: inset 0 0 0 2px var(--gold-light);
    text-align: center;
  }

  /* Front label */
  .front-label .brand-block {
    position: absolute;
    top: 70px;
    left: 0;
    right: 0;
    display: flex;
    flex-direction: column;
    align-items: center;
    gap: 18px;
  }
  .brand-mark {
    width: 14px;
    height: 14px;
    background: var(--plum);
  }
  .brand-name {
    font-family: "EB Garamond", serif;
    font-weight: 500;
    font-size: 54px;
    line-height: 1;
    color: var(--plum);
    letter-spacing: 1px;
  }
  .front-label .specs {
    position: absolute;
    top: 318px;
    left: 34px;
    right: 34px;
    display: flex;
    justify-content: space-between;
    font-family: "EB Garamond", serif;
    font-style: italic;
    font-weight: 500;
    font-size: 25px;
    color: var(--gold-text);
  }
  .front-label .vintage {
    position: absolute;
    top: 380px;
    left: 0;
    right: 0;
    font-family: "EB Garamond", serif;
    font-style: italic;
    font-weight: 500;
    font-size: 25px;
    color: var(--gold-text);
  }
  .front-label .bottling {
    position: absolute;
    bottom: 28px;
    left: 0;
    right: 0;
    font-family: "EB Garamond", serif;
    font-style: italic;
    font-size: 22px;
    color: var(--ink);
  }

  /* Back label */
  .back-label {
    padding: 42px 26px 0;
    font-family: "Nunito Sans", sans-serif;
    color: var(--ink-soft);
  }
  .back-label h2 {
    font-size: 14px;
    font-weight: 700;
    color: var(--plum);
    letter-spacing: 0.3px;
    margin-bottom: 20px;
  }
  .analysis-list {
    list-style: none;
    font-size: 13px;
    line-height: 27px;
    margin-bottom: 40px;
  }
  .vineyards-text {
    font-size: 13px;
    line-height: 26px;
  }
  .back-brand {
    position: absolute;
    bottom: 22px;
    left: 0;
    right: 0;
    display: flex;
    justify-content: center;
    align-items: center;
    gap: 8px;
  }
  .back-brand .brand-mark { width: 9px; height: 9px; }
  .back-brand .brand-name { font-size: 22px; letter-spacing: 0.5px; }
</style>
</head>
<body>
  <main class="canvas">
    <section class="label front-label" aria-label="Front label">
      <div class="brand-block">
        <span class="brand-mark"></span>
        <span class="brand-name">Kowhai Lane</span>
      </div>
      <div class="specs">
        <span class="abv">12% vol.</span>
        <span class="volume">75 cl</span>
      </div>
      <div class="vintage">2008</div>
      <div class="bottling">Mis en Bouteille au Chateau</div>
    </section>

    <section class="label back-label" aria-label="Back label">
      <h2>TECHNICAL ANALYSIS</h2>
      <ul class="analysis-list">
        <li>pH: 3.77</li>
        <li>Total acidity as tartaric: 5.3g/l</li>
        <li>Alcohol: 14.0%</li>
        <li>Residual Sugar: Dry</li>
      </ul>
      <h2>VINEYARDS</h2>
      <p class="vineyards-text">Separate parcels of fully ripened pinot noir grapes were hand-harvested from Pirovane Estate’s Ashgrove Vineyards between 3 and 17 March 2018.</p>
      <div class="back-brand">
        <span class="brand-mark"></span>
        <span class="brand-name">Kowhai Lane</span>
      </div>
    </section>
  </main>
</body>
</html>
```